Re Design of Business Cards

We a Technology & Telecommunications company, we supply computer repairs suppy and services to home and business's, we also a Telecommunications company as well and that we supply Internet, Mobile Voice and Data and Voice Lines to home and business as well we want to get our business cards re designed that stand out but also state what we can do and that we also come to you, there is 4 of us in the business so we all need same business card design but just different names and phone numbers on all.
Ive upload our Logo as well. and current looking business cards.

Our current business cards does not make me excited and or stand out, to dark and does not say what we do, we leave our business cards in letter boxes some times and in receptions of villages for retiress so the reception can hand out, few times now there asked what do you do, so thinking one side is our contact details and other is our services

I think I like to also put our address onto it as well, very simple as its also my home address but it be good to have it on there

48 Pellow St - Kelby Shores NSW 2199

We should also have our business rego number which is a ABN

ABN: 37 904 516 283

this way we all covered and we look very Professional

We would like to make some Points, 1st of All we just found out we do not need out ABN on our Business Cards so we can Remove that please

we would like the address for the business to be on cards as well,

On the flip side of the Business Cards we would like to list some of our services as below

High-Speed Internet for Home & Business
Managed IT Services & Support
Network Setup & Optimization
VoIP & Mobile Voice Solutions
Wi-Fi Installation & Troubleshooting
Smart Home & Office Technology
Data Backup & Cybersecurity
Onsite Home and Or Business

```html
<!DOCTYPE html>
<html lang="en">
<head>
<meta charset="utf-8">
<title>Corvane Business Cards</title>
<link rel="stylesheet" href="https://fonts.googleapis.com/css2?family=Poppins:wght@400;500;600;700&display=swap">
<style>
  :root {
    --canvas: #2a2a2c;
    --card: #06363a;
    --orange: #f26a21;
    --green: #1fc21f;
    --white: #ffffff;
  }
  * { box-sizing: border-box; margin: 0; padding: 0; }
  html, body {
    width: 1200px; height: 1189px; overflow: hidden;
    background: var(--canvas);
    font-family: "Poppins", sans-serif;
    color: var(--white);
  }
  .sheet {
    position: relative; width: 1200px; height: 1189px;
    display: flex; flex-direction: column; align-items: center;
    justify-content: center; gap: 70px;
  }
  .card {
    position: relative; width: 880px; height: 500px;
    background: var(--card); border-radius: 34px;
    box-shadow: 0 14px 30px rgba(0,0,0,.45);
    overflow: hidden;
  }
  /* Services side */
  .services { padding: 62px 70px; }
  .brand {
    font-weight: 700; color: var(--orange);
    letter-spacing: 10px; line-height: 1;
  }
  .services .brand { font-size: 52px; }
  .services-title {
    margin-top: 34px; font-size: 22px; font-weight: 600;
    color: var(--orange); letter-spacing: 1px;
  }
  .service-list { list-style: none; margin-top: 14px; }
  .service-list li {
    display: flex; align-items: center; gap: 16px;
    font-size: 21px; font-weight: 500; line-height: 33px;
  }
  .service-list li::before {
    content: ""; width: 13px; height: 13px; border-radius: 50%;
    background: var(--green); flex: none;
  }
  /* Contact side */
  .contact { display: flex; align-items: center; }
  .contact-brand {
    width: 430px; display: flex; justify-content: center;
  }
  .contact .brand { font-size: 50px; }
  .divider {
    width: 2px; height: 290px; background: var(--green);
  }
  .details { padding-left: 52px; }
  .person { font-size: 27px; font-weight: 700; letter-spacing: 1px; line-height: 1.1; }
  .role { font-size: 20px; color: var(--orange); font-weight: 500; margin-bottom: 20px; }
  .address { font-size: 20px; font-weight: 500; line-height: 30px; margin-bottom: 18px; }
  .lines { list-style: none; }
  .lines li {
    display: flex; align-items: center; gap: 14px;
    font-size: 20px; font-weight: 500; line-height: 36px;
  }
  .icon {
    width: 24px; height: 24px; border-radius: 50%; background: var(--orange);
    display: flex; align-items: center; justify-content: center; flex: none;
  }
  .abn { margin-top: 24px; font-size: 22px; font-weight: 600; }
  .abn span { color: var(--orange); }
</style>
</head>
<body>
<main class="sheet">
  <section class="card services">
    <div class="brand">CORVANE</div>
    <h2 class="services-title">OUR SERVICES</h2>
    <ul class="service-list">
      <li>High-Speed Internet for Home &amp; Business</li>
      <li>Managed IT Services &amp; Support</li>
      <li>Network Setup &amp; Optimization</li>
      <li>VoIP &amp; Mobile Voice Solutions</li>
      <li>Wi-Fi Installation &amp; Troubleshooting</li>
      <li>Smart Home &amp; Office Technology</li>
      <li>Data Backup &amp; Cybersecurity</li>
      <li>Onsite Home and Or Business</li>
    </ul>
  </section>

  <section class="card contact">
    <div class="contact-brand">
      <div class="brand">CORVANE</div>
    </div>
    <div class="divider"></div>
    <div class="details">
      <div class="person">SAM TORRICK</div>
      <div class="role">Sales Consultant</div>
      <div class="address">48 Pellow St<br>Kelby Shores NSW 2199</div>
      <ul class="lines">
        <li><span class="icon"><svg width="12" height="12" viewBox="0 0 24 24"><path fill="#fff" d="M6.6 10.8a15 15 0 0 0 6.6 6.6l2.2-2.2c.3-.3.7-.4 1-.2 1.1.4 2.3.6 3.6.6.6 0 1 .4 1 1V20c0 .6-.4 1-1 1A17 17 0 0 1 3 4c0-.6.4-1 1-1h3.5c.6 0 1 .4 1 1 0 1.3.2 2.5.6 3.6.1.3 0 .7-.2 1z"/></svg></span>1800 555 014</li>
        <li><span class="icon"><svg width="12" height="12" viewBox="0 0 24 24"><rect x="6" y="2" width="12" height="20" rx="2" fill="none" stroke="#fff" stroke-width="2.5"/></svg></span>0400 555 182</li>
        <li><span class="icon"><svg width="12" height="12" viewBox="0 0 24 24"><rect x="2" y="5" width="20" height="14" rx="1" fill="none" stroke="#fff" stroke-width="2.2"/><path d="M2 6l10 7 10-7" fill="none" stroke="#fff" stroke-width="2.2"/></svg></span>sam@corvane.com.au</li>
      </ul>
      <div class="abn"><span>ABN:</span> 37 904 516 283</div>
    </div>
  </section>
</main>
</body>
</html>
```